Redesign of Current Wix Website - Event Production Company

Our website is www.trulvanshows.com and we need a redesign. We are full service event production company offering clients services including event management, graphics and content creation, vendor sourcing and management, contract review, audio visual production and venue selection. We would like our website to look more like an event management company, not just an audio visual company which it looks like now.
We want to look more like www.basquirelabs.com
Our Wix account is FILLED with logos, pictures and all the graphics you will need and we can assist with assets, categories and text.
On the Logo, I want to move away from "Halvindor Stage Production" and move to "Halvindor Stage Production" and I would like a redesigned logo with the same center element but a name change. I do have the art work files for the logo, vector and ai.

Target Market(s)

Event Planners and people that book event services. Assistants of CEOs. Marketing Directors. Gala Chairpersons and people in positions to purchase large scale event production

Industry/Entity Type

Event Management and Production - Corporate and Social

Coding

Coded - Design and coding required

Font styles to use
Other font styles liked:
• my logo is multicolor. look at it before you design

Colors
0054AA
0677BA
7BADD7
CADEEF
E8F1F8
6B429C
8869AF
B7A5CE
E3DAEB
F3F0F8

Requirements
Must have
• A clean professional look that shows the client who we are and what we do, and the full scope of what we do.
Nice to have
• www.basquirelabs.com ; https://themarbledrift.com/ look at these two website We are going after venues, planners end clients. Much like the on service page.

```html
<!DOCTYPE html>
<html lang="en">
<head>
<meta charset="utf-8">
<title>Halvindor Stage Production — Event Production</title>
<link rel="stylesheet" href="https://fonts.googleapis.com/css2?family=Plus+Jakarta+Sans:wght@400;500;600;700;800&display=swap">
<style>
:root{
  --blue-deep:#0054aa;
  --blue:#0677ba;
  --blue-soft:#7badd7;
  --blue-pale:#cadeef;
  --purple:#6b429c;
  --purple-mid:#8869af;
  --white:#ffffff;
  --ink:#333333;
  --grey:#8a8a8a;
  --form-bg:rgba(215,215,225,.88);
}
*{box-sizing:border-box;margin:0;padding:0}
html,body{width:1200px;height:4444px;overflow:hidden}
body{font-family:"Plus Jakarta Sans",sans-serif;color:var(--ink);background:var(--white);position:relative}
section,footer{position:absolute;left:0;width:1200px}
.btn{position:absolute;display:flex;align-items:center;justify-content:center;border-radius:28px;font-weight:700;font-size:16px;color:var(--white);background:var(--purple);text-decoration:none}

/* hero */
.hero{top:0;height:581px;background:radial-gradient(ellipse at 50% 20%,#6b5a4a 0%,#2a211c 45%,#120e0c 100%)}
.hero-shade{position:absolute;inset:0;background:rgba(0,0,0,.35)}
.socials{position:absolute;display:flex;gap:8px}
.socials span{width:34px;height:34px;border-radius:50%;background:var(--blue-soft);display:block}
.hero .socials{left:141px;top:43px}
.brand-mark{position:absolute;left:567px;top:22px;width:66px;height:66px;border-radius:50%;background:#111;border:2px solid var(--white);display:flex;align-items:center;justify-content:center;color:var(--white);font-size:10px;font-weight:700;text-align:center;line-height:12px}
.phone{position:absolute;right:140px;top:49px;color:var(--white);font-size:15px;display:flex;align-items:center;gap:5px}
.nav{position:absolute;top:98px;left:0;width:1200px;display:flex;justify-content:center;gap:16px}
.nav a{color:var(--white);font-size:15px;text-decoration:none}
.hero h1{position:absolute;top:185px;left:0;width:1200px;text-align:center;color:var(--white);font-size:66px;line-height:86px;font-weight:800;letter-spacing:-1px}
.hero p{position:absolute;top:366px;left:295px;width:610px;text-align:center;color:var(--white);font-size:17px;line-height:23px}
.hero .btn{left:517px;top:444px;width:167px;height:52px}

/* intro */
.intro{top:581px;height:516px;background:var(--white)}
.intro-photo{position:absolute;left:141px;top:78px;width:362px;height:362px;border-radius:50%;border:5px solid var(--blue-soft);background:linear-gradient(135deg,#2b2f9a,#5b2fb0 45%,#1c1a3a)}
.intro h2{position:absolute;left:529px;top:110px;color:var(--purple);font-size:39px;font-weight:600}
.intro p{position:absolute;left:529px;top:178px;width:520px;font-size:16.5px;line-height:22.5px;color:#444}
.intro .btn{left:529px;top:320px;width:167px;height:52px}

/* services */
.services{top:1097px;height:1496px;background:linear-gradient(160deg,#143f74,#0f3566 50%,#0b2d5a)}
.services h2{position:absolute;top:46px;width:1200px;text-align:center;color:var(--white);font-size:38px;font-weight:500}
.svc-row{position:absolute;left:0;width:1200px;height:406px}
.svc-photo{position:absolute;top:0;width:600px;height:406px}
.svc-text{position:absolute;top:0;width:600px;height:406px;padding:0 0 0 139px;display:flex;flex-direction:column;justify-content:center;color:var(--white)}
.svc-text.right{padding-left:26px}
.svc-text h3{font-size:23px;font-weight:500;margin-bottom:22px}
.svc-text p{font-size:14.5px;line-height:22.5px;width:445px}
.svc-text a{color:var(--white);font-size:16px;font-weight:700;text-decoration:none;margin-top:26px}
.services .btn{left:517px;top:1382px;width:167px;height:52px;background:var(--blue-pale);color:var(--blue-deep)}

/* video */
.video{top:2593px;height:661px;background:var(--white)}
.video-frame{position:absolute;left:218px;top:74px;width:764px;height:429px;border-radius:12px;background:linear-gradient(120deg,#3a3a36,#5b5a52 40%,#2d3240);overflow:hidden}
.play{position:absolute;left:344px;top:168px;width:76px;height:76px;border-radius:50%;background:var(--white);display:flex;align-items:center;justify-content:center}
.video-title{position:absolute;left:0;bottom:30px;width:764px;text-align:center;color:var(--white);font-size:21px;font-weight:700}
.video .btn{left:506px;top:531px;width:189px;height:53px}

/* testimonial */
.testimonial{top:3254px;height:381px;background:linear-gradient(180deg,#163f70,#1f4a80)}
.testimonial h2{position:absolute;top:48px;width:1200px;text-align:center;color:var(--white);font-size:40px;font-weight:500}
.testimonial blockquote{position:absolute;top:118px;left:290px;width:620px;text-align:center;color:var(--white);font-size:21.5px;line-height:30px;font-weight:600}
.testimonial cite{position:absolute;top:326px;width:1200px;text-align:center;color:var(--white);font-style:normal;font-size:16px}

/* contact */
.contact{top:3635px;height:512px;background:linear-gradient(135deg,#2b1f48,#3f2a60 50%,#231a3b)}
.contact-mark{position:absolute;left:148px;top:108px;width:290px;height:290px;border-radius:50%;background:#0e0e12;border:6px solid #e5e5e5;display:flex;align-items:center;justify-content:center;text-align:center;color:var(--white);font-size:28px;line-height:36px;font-weight:700;padding:30px}
.form{position:absolute;left:609px;top:60px;width:450px;height:395px;border-radius:12px;background:var(--form-bg)}
.field{position:absolute;border-bottom:1px solid #777;font-size:14.5px;color:#444;padding-bottom:8px}
.form .btn{left:18px;top:300px;width:100px;height:52px}

/* footer */
.footer{top:4147px;height:297px;background:var(--white)}
.footer-brand{position:absolute;left:120px;top:45px;width:250px;display:flex;flex-direction:column;align-items:center;gap:10px}
.footer-brand .dot{width:90px;height:90px;border-radius:50%;background:#111;border:3px solid #ccc}
.footer-brand span{font-size:17px;color:var(--grey);letter-spacing:1px;text-align:center;line-height:22px}
.footer h4{position:absolute;top:52px;font-size:22px;font-weight:500;color:#333}
.links{position:absolute;left:506px;top:104px;list-style:none}
.links li{font-size:14.5px;color:var(--grey);line-height:30px}
.footer .phone{position:static;color:var(--grey);font-size:14.5px}
.foot-contact{position:absolute;left:767px;top:104px;display:flex;flex-direction:column;gap:14px}
.foot-contact .socials{position:static}
.copy{font-size:13px;color:var(--grey)}
</style>
</head>
<body>

<section class="hero">
  <div class="hero-shade" role="img" aria-label="Concert crowd with raised hands under stage lights"></div>
  <div class="socials" aria-label="Social links"><span></span><span></span><span></span></div>
  <div class="brand-mark">Halvindor</div>
  <div class="phone"><svg width="12" height="12" viewBox="0 0 24 24"><path fill="#fff" d="M6.6 10.8a15 15 0 006.6 6.6l2.2-2.2a1 1 0 011-.25 11.4 11.4 0 003.6.57 1 1 0 011 1V20a1 1 0 01-1 1A17 17 0 013 4a1 1 0 011-1h3.5a1 1 0 011 1 11.4 11.4 0 00.57 3.6 1 1 0 01-.25 1z"/></svg>(888) 555-0142</div>
  <nav class="nav"><a>About</a><a>Event Production</a><a>Content Creation</a><a>Halvindor Social Media</a><a>Get A Quote</a></nav>
  <h1>ELEVATING EXPERIENCES,<br>FLAWLESSLY</h1>
  <p>We guarantee that each event we create will live up to your expectations and leave a lasting impression.</p>
  <a class="btn">KNOW MORE</a>
</section>

<section class="intro">
  <div class="intro-photo" role="img" aria-label="Speaker at a podium before a gala audience with purple stage screens"></div>
  <h2>Event Production</h2>
  <p>Halvindor Stage Production LLC is a full-service event production company that specializes in creating amazing experiences for our clients. We are dedicated to helping you bring your vision to life through our expert audio visual, planning, logistics, lighting, staging, and design services.</p>
  <a class="btn">KNOW MORE</a>
</section>

<section class="services">
  <h2>Our Services</h2>
  <div class="svc-row" style="top:131px">
    <div class="svc-text" style="left:0">
      <h3>AUDIO VISUAL PRODUCTION</h3>
      <p>Audio Visual is the foundation of any successful event. Halvindor has over 20 years of expertise in Audio Visual contracting, staffing and equipment allocation.</p>
      <a>KNOW MORE &gt;</a>
    </div>
    <div class="svc-photo" style="left:600px;background:linear-gradient(135deg,#8d8a82,#4b4a48 50%,#222)" role="img" aria-label="Ballroom with camera and video switching equipment"></div>
  </div>
  <div class="svc-row" style="top:537px">
    <div class="svc-photo" style="left:0;background:linear-gradient(160deg,#2b3d7c,#5d4f55 50%,#6e6459)" role="img" aria-label="Banquet hall with seated guests and stage screens"></div>
    <div class="svc-text right" style="left:600px">
      <h3>EVENT CONSULTING &amp; MANAGEMENT</h3>
      <p>Halvindor Stage Production works with local and national clients, consulting on several aspects of the meeting, conference and gala planning process.</p>
      <a>KNOW MORE &gt;</a>
    </div>
  </div>
  <div class="svc-row" style="top:943px">
    <div class="svc-text" style="left:0">
      <h3>HYBRID: LIVE &amp; VIRTUAL EVENT SERVICES</h3>
      <p>Welcome to Halvindor Stage Production, your premier provider of Hybrid Event Services that expertly integrate complex audio visual systems with current virtual meeting technology.</p>
      <a>KNOW MORE &gt;</a>
    </div>
    <div class="svc-photo" style="left:600px;background:linear-gradient(135deg,#4a6ea8,#c9d6e6 50%,#6a88b3)" role="img" aria-label="Trade show exhibit booth with display screens"></div>
  </div>
  <a class="btn">KNOW MORE</a>
</section>

<section class="video">
  <div class="video-frame" role="img" aria-label="Video still from a hotel grand opening interview">
    <div class="play"><svg width="30" height="22" viewBox="0 0 30 22"><rect width="30" height="22" rx="6" fill="#0b3b7a"/><path d="M12 6l8 5-8 5z" fill="#fff"/></svg></div>
    <div class="video-title">HOTEL MARROWIND GRAND OPENING - ASHBURY GA</div>
  </div>
  <a class="btn">SEE ALL VIDEOS</a>
</section>

<section class="testimonial">
  <h2>Testimonial</h2>
  <blockquote>I wanted to thank you and your team for doing an excellent job with the set up for the red carpet award night. the stage looked amazing and your efforts help us make the event memorable. We truly appreciate your professionalism, quick turnaround and quality of work …<br>Job well done!!</blockquote>
  <cite>- Crestline Advisory</cite>
</section>

<section class="contact" role="img" aria-label="Dim event hall with purple lighting">
  <div class="contact-mark">Halvindor Stage Production</div>
  <form class="form">
    <div class="field" style="left:33px;top:40px;width:180px">First Name</div>
    <div class="field" style="left:266px;top:40px;width:165px">Last Name</div>
    <div class="field" style="left:33px;top:99px;width:180px">Email</div>
    <div class="field" style="left:266px;top:99px;width:165px">Phone</div>
    <div class="field" style="left:18px;top:158px;width:413px">Mail Subject</div>
    <div class="field" style="left:18px;top:216px;width:413px;height:60px">Your Message</div>
    <a class="btn">SEND</a>
  </form>
</section>

<footer class="footer">
  <div class="footer-brand"><div class="dot"></div><span>HALVINDOR<br>STAGE PRODUCTION</span></div>
  <h4 style="left:506px">Quick Links</h4>
  <ul class="links"><li>About</li><li>Event Production</li><li>Content Creation</li><li>Halvindor Social Media</li><li>Get A Quote</li></ul>
  <h4 style="left:767px">Contact</h4>
  <div class="foot-contact">
    <div class="phone"><svg width="12" height="12" viewBox="0 0 24 24"><path fill="#8a8a8a" d="M6.6 10.8a15 15 0 006.6 6.6l2.2-2.2a1 1 0 011-.25 11.4 11.4 0 003.6.57 1 1 0 011 1V20a1 1 0 01-1 1A17 17 0 013 4a1 1 0 011-1h3.5a1 1 0 011 1 11.4 11.4 0 00.57 3.6 1 1 0 01-.25 1z"/></svg> (888) 555-0142</div>
    <div class="socials" aria-label="Social links"><span></span><span></span><span></span></div>
    <div class="copy">© 2025 Halvindor Stage Production. All Rights Reserved.</div>
  </div>
</footer>

</body>
</html>
```